Football field themed poster-game

I'm looking for a 22" x 29" size poster with a minimum of 300dpi, max of 300mb. File format can be jpg, gif, tiff or bmp. Would like the field portion of the poster to appear like a real grass football field. The field will need makers for each yard. I've added an addition simple clip art that shows another way for yard lines as well.The rest of the layout I would like similar, but made to look more professional. Wording should be the same as in the given draft and located in the same area or close to that area on the poster. The style is open, but should be a little minimalist in nature. Design work has to be original and cannot be taken from trademarked or copyrighted items.
Updates

Project Deadline Extended
Reason: I have 2 or 3 designs that really standout, but I would like to see just a few more.

Target Market(s)

Football fans

Font styles to use
Sans Serif

Colors

Designer to choose colors to be used in the design.

Requirements
Must have
• The design must have the same similar layout as the file I have submitted with the contest. The football field needs to be made to look like a real field with turf. boarders would be nice and a modern look.
Should not have
• hard to read fonts, changes to the major overall layout of poster.

```html
<!DOCTYPE html>
<html lang="en">
<head>
<meta charset="utf-8">
<title>Kickoff Cup Football Poster Game</title>
<link href="https://fonts.googleapis.com/css2?family=Russo+One&display=swap" rel="stylesheet">
<style>
  :root {
    --page-bg: #d9d9de;
    --poster-white: #ffffff;
    --brown-light: #9a5a3a;
    --brown-dark: #6e3418;
    --token-orange: #dd9a50;
    --team-blue: #215da3;
    --turf-light: #6aa13a;
    --turf-dark: #3f7a22;
    --line-white: #ffffff;
    --ink: #111111;
  }
  html, body {
    margin: 0;
    width: 1200px;
    height: 1200px;
    overflow: hidden;
    background: var(--page-bg);
  }
  .poster {
    position: absolute;
    left: 168px;
    top: 30px;
    width: 864px;
    height: 1140px;
    display: block;
  }
  .label-text, .yard-number, .event-name {
    font-family: "Russo One", sans-serif;
  }
  .label-text { fill: var(--ink); font-size: 40px; }
  .yard-number { fill: var(--line-white); font-size: 46px; }
  .event-name { fill: var(--poster-white); font-size: 54px; }
</style>
</head>
<body>
<svg class="poster" viewBox="0 0 910 1200" xmlns="http://www.w3.org/2000/svg">
  <defs>
    <linearGradient id="brownPanel" x1="0" y1="0" x2="1" y2="1">
      <stop offset="0" stop-color="var(--brown-dark)"/>
      <stop offset="0.4" stop-color="var(--brown-light)"/>
      <stop offset="1" stop-color="var(--brown-dark)"/>
    </linearGradient>
    <linearGradient id="turf" x1="0" y1="0" x2="1" y2="1">
      <stop offset="0" stop-color="var(--turf-light)"/>
      <stop offset="0.5" stop-color="var(--turf-dark)"/>
      <stop offset="1" stop-color="var(--turf-light)"/>
    </linearGradient>
    <pattern id="hashMarks" patternUnits="userSpaceOnUse" width="10" height="9.27" y="228">
      <rect x="0" y="0" width="10" height="2" fill="var(--line-white)"/>
    </pattern>
  </defs>

  <rect class="sheet" x="0" y="0" width="910" height="1200" fill="var(--poster-white)"/>

  <g class="score-panel">
    <rect x="8" y="8" width="347" height="1184" fill="url(#brownPanel)" role="img" aria-label="Brown faceted geometric backdrop"/>
    <circle cx="179" cy="155" r="103" fill="var(--token-orange)"/>
    <rect x="112" y="88" width="134" height="134" fill="var(--poster-white)"/>
    <rect x="59" y="313" width="240" height="67" fill="var(--poster-white)"/>
    <text class="label-text" x="179" y="362" text-anchor="middle" transform="rotate(180 179 346)">SCORE</text>

    <g class="event-title" text-anchor="middle">
      <text class="event-name" x="179" y="585">KICKOFF</text>
      <text class="event-name" x="179" y="660">CUP</text>
    </g>

    <rect x="59" y="816" width="240" height="67" fill="var(--poster-white)"/>
    <text class="label-text" x="179" y="865" text-anchor="middle">SCORE</text>
    <circle cx="179" cy="1042" r="103" fill="var(--token-orange)"/>
    <rect x="112" y="975" width="134" height="134" fill="var(--poster-white)"/>
  </g>

  <g class="home-band">
    <rect x="363" y="8" width="539" height="130" fill="var(--team-blue)"/>
    <rect x="429" y="40" width="405" height="67" fill="var(--poster-white)"/>
    <text class="label-text" x="631" y="89" text-anchor="middle" transform="rotate(180 631 73)">HOME</text>
  </g>

  <g class="field">
    <rect x="363" y="142" width="539" height="918" fill="url(#turf)" role="img" aria-label="Real grass turf texture"/>
    <rect class="hash-left" x="417" y="148" width="105" height="906" fill="url(#hashMarks)"/>
    <rect class="hash-right" x="740" y="148" width="105" height="906" fill="url(#hashMarks)"/>
    <g class="five-yard-lines" stroke="var(--line-white)" stroke-width="2">
      <line x1="380" y1="182" x2="557" y2="182"/><line x1="705" y1="182" x2="880" y2="182"/>
      <line x1="380" y1="275" x2="557" y2="275"/><line x1="705" y1="275" x2="880" y2="275"/>
      <line x1="380" y1="367" x2="557" y2="367"/><line x1="705" y1="367" x2="880" y2="367"/>
      <line x1="380" y1="460" x2="557" y2="460"/><line x1="705" y1="460" x2="880" y2="460"/>
      <line x1="380" y1="553" x2="557" y2="553"/><line x1="705" y1="553" x2="880" y2="553"/>
      <line x1="380" y1="645" x2="557" y2="645"/><line x1="705" y1="645" x2="880" y2="645"/>
      <line x1="380" y1="738" x2="557" y2="738"/><line x1="705" y1="738" x2="880" y2="738"/>
      <line x1="380" y1="831" x2="557" y2="831"/><line x1="705" y1="831" x2="880" y2="831"/>
      <line x1="380" y1="924" x2="557" y2="924"/><line x1="705" y1="924" x2="880" y2="924"/>
      <line x1="380" y1="1016" x2="557" y2="1016"/><line x1="705" y1="1016" x2="880" y2="1016"/>
    </g>
    <g class="ten-yard-lines" stroke="var(--line-white)" stroke-width="2.5">
      <line x1="363" y1="229" x2="590" y2="229"/><line x1="676" y1="229" x2="902" y2="229"/>
      <line x1="363" y1="321" x2="590" y2="321"/><line x1="676" y1="321" x2="902" y2="321"/>
      <line x1="363" y1="414" x2="590" y2="414"/><line x1="676" y1="414" x2="902" y2="414"/>
      <line x1="363" y1="507" x2="590" y2="507"/><line x1="676" y1="507" x2="902" y2="507"/>
      <line x1="363" y1="599" x2="590" y2="599"/><line x1="676" y1="599" x2="902" y2="599"/>
      <line x1="363" y1="692" x2="590" y2="692"/><line x1="676" y1="692" x2="902" y2="692"/>
      <line x1="363" y1="785" x2="590" y2="785"/><line x1="676" y1="785" x2="902" y2="785"/>
      <line x1="363" y1="877" x2="590" y2="877"/><line x1="676" y1="877" x2="902" y2="877"/>
      <line x1="363" y1="970" x2="590" y2="970"/><line x1="676" y1="970" x2="902" y2="970"/>
    </g>
    <g class="yard-numbers" text-anchor="middle">
      <text class="yard-number" x="633" y="245" transform="rotate(180 633 229)">10</text>
      <text class="yard-number" x="633" y="337" transform="rotate(180 633 321)">20</text>
      <text class="yard-number" x="633" y="430" transform="rotate(180 633 414)">30</text>
      <text class="yard-number" x="633" y="523" transform="rotate(180 633 507)">40</text>
      <text class="yard-number" x="633" y="615" transform="rotate(180 633 599)">50</text>
      <text class="yard-number" x="633" y="708">40</text>
      <text class="yard-number" x="633" y="801">30</text>
      <text class="yard-number" x="633" y="893">20</text>
      <text class="yard-number" x="633" y="986">10</text>
    </g>
  </g>

  <g class="visitors-band">
    <rect x="363" y="1064" width="539" height="128" fill="var(--team-blue)"/>
    <rect x="429" y="1094" width="405" height="68" fill="var(--poster-white)"/>
    <text class="label-text" x="631" y="1144" text-anchor="middle">VISITORS</text>
  </g>
</svg>
</body>
</html>
```